Dietitian needs awesome business card

I need a contemporary design that's eye catching but professional.
My card is to given to doctors, specialists and patients alike.
I manage patients with chronic diseases
I have uploaded my logo and current business card, I would also like the other Registered Clinical Nutritionist logo incorporated into the design

Target Market(s)

Doctors, specialists and patients

Industry/Entity Type

Healthcare

Contact Information for Business Card

www.brindlecovenutrition.com.au
Ph: 0427 516 903
Fax: 6482 7315
email: marcus.k.wellfare@quorvamail.com
Space on the back of the card with: Appointment date, Appointment time and appointment location

Font styles to use
Serif

Colors
fbee3e
876aae
ffc214

Requirements
Must have
• My Logo
• Registered Clinical Nutritionist Logo
• My 4 locations - Fernhollow Medical Centre, North Kelby Health, Ashcourt Medical, Pinebrook Doctors Surgery
Nice to have
• I like the colours in my current business card

```html
<!DOCTYPE html>
<html lang="en">
<head>
<meta charset="utf-8">
<title>Brindlecove Nutrition &amp; Dietetics – Business Card</title>
<link href="https://fonts.googleapis.com/css2?family=Open+Sans:wght@400;600;700&family=Libre+Baskerville:ital@0;1&display=swap" rel="stylesheet">
<style>
  :root {
    --page: #ecebe7;
    --card: #ffffff;
    --blue: #1283c4;
    --blue-light: #19a9dc;
    --blue-deep: #2a3f9e;
    --green: #8cc63f;
    --green-light: #c4e03a;
    --ink: #2b5db8;
    --muted: #5a6f86;
    --badge: #f0822e;
    --rule: #2f4f8f;
  }
  * { box-sizing: border-box; margin: 0; padding: 0; }
  html, body { width: 1200px; height: 1023px; overflow: hidden; }
  body {
    background: var(--page);
    font-family: "Open Sans", Arial, sans-serif;
    display: flex; flex-direction: column; align-items: center; justify-content: center;
    gap: 60px;
  }
  .card {
    position: relative; width: 700px; height: 400px;
    background: var(--card); border-radius: 16px; overflow: hidden;
    box-shadow: 0 6px 18px rgba(0,0,0,.15);
  }
  .card-art { position: absolute; inset: 0; }

  /* front */
  .brand { position: absolute; left: 40px; top: 150px; display: flex; align-items: center; gap: 14px; }
  .brand-dot { width: 64px; height: 64px; border-radius: 50%; background: var(--blue); }
  .brand-name { color: var(--ink); font-weight: 400; line-height: 1.05; }
  .brand-name .main { display: block; font-size: 44px; letter-spacing: -1px; }
  .brand-name .sub { display: block; font-size: 19px; }
  .person { position: absolute; right: 250px; top: 42px; text-align: right; }
  .person-name { color: var(--ink); font-size: 27px; font-weight: 700; }
  .person-title { color: var(--green); font-size: 14px; margin-top: 2px; }
  .contacts { position: absolute; left: 60px; bottom: 48px; list-style: none; }
  .contacts li { display: flex; align-items: center; gap: 9px; color: var(--muted); font-size: 13px; line-height: 24px; white-space: nowrap; }
  .contacts svg { width: 13px; height: 13px; flex: none; }
  .badge { position: absolute; right: 44px; top: 48px; width: 70px; height: 52px; background: var(--badge); border-radius: 3px; }

  /* back */
  .back { display: flex; }
  .back-edge { width: 44px; background: linear-gradient(180deg, var(--blue-light), var(--blue)); }
  .back-form { width: 380px; padding: 40px 36px 0 38px; font-family: "Libre Baskerville", Georgia, serif; }
  .back-title { color: var(--blue-light); font-style: italic; font-size: 28px; margin-bottom: 28px; }
  .field { display: flex; align-items: flex-end; gap: 10px; font-style: italic; color: var(--rule); font-size: 14px; margin-bottom: 26px; }
  .field .line { flex: 1; border-bottom: 1px solid var(--rule); height: 1px; }
  .back-brand {
    flex: 1; background: linear-gradient(160deg, var(--blue-light), var(--blue));
    display: flex; align-items: center; justify-content: center; gap: 14px; color: #fff;
  }
  .back-brand .brand-dot { background: #fff; width: 58px; height: 58px; }
  .back-brand .brand-name { color: #fff; }
  .back-brand .brand-name .main { font-size: 36px; }
  .back-brand .brand-name .sub { font-size: 16px; }
</style>
</head>
<body>

<section class="card front" aria-label="Business card front">
  <svg class="card-art" viewBox="0 0 700 400" preserveAspectRatio="none" aria-hidden="true">
    <defs>
      <linearGradient id="frontBlue" x1="0" y1="0" x2="0" y2="1">
        <stop offset="0" stop-color="#19a9dc"/>
        <stop offset=".6" stop-color="#1283c4"/>
        <stop offset="1" stop-color="#2a3f9e"/>
      </linearGradient>
    </defs>
    <path d="M500 0 C470 170 420 320 300 400 L700 400 L700 0 Z" fill="url(#frontBlue)"/>
    <path d="M488 0 C458 170 408 318 282 400" fill="none" stroke="#c4e03a" stroke-width="6"/>
    <path d="M480 0 C450 170 398 316 268 400" fill="none" stroke="#8cc63f" stroke-width="4"/>
  </svg>

  <div class="brand">
    <span class="brand-dot"></span>
    <span class="brand-name"><span class="main">Brindlecove</span><span class="sub">Nutrition &amp; Dietetics</span></span>
  </div>

  <div class="person">
    <p class="person-name">Marcus Wellfare</p>
    <p class="person-title">Registered Clinical Nutritionist</p>
  </div>

  <div class="badge" aria-label="Professional accreditation badge"></div>

  <ul class="contacts">
    <li><svg viewBox="0 0 16 16"><circle cx="8" cy="8" r="7" fill="none" stroke="#8cc63f" stroke-width="1.5"/><path d="M6 4.5l1.5 2-1 1c.5 1 1.3 1.8 2.3 2.3l1-1 2 1.5-1 1.2C8 11 5 8 4.8 5.5z" fill="#8cc63f"/></svg>0427 516 903</li>
    <li><svg viewBox="0 0 16 16"><rect x="2" y="5" width="12" height="8" rx="1" fill="#8cc63f"/><rect x="4" y="2" width="8" height="4" fill="#8cc63f"/></svg>6482 7315</li>
    <li><svg viewBox="0 0 16 16"><circle cx="8" cy="8" r="7" fill="none" stroke="#8cc63f" stroke-width="1.5"/><path d="M1 8h14M8 1c-3 3-3 11 0 14M8 1c3 3 3 11 0 14" fill="none" stroke="#8cc63f" stroke-width="1.2"/></svg>www.brindlecovenutrition.com.au</li>
  </ul>
</section>

<section class="card back" aria-label="Business card back">
  <div class="back-edge"></div>
  <div class="back-form">
    <p class="back-title">Appointment</p>
    <div class="field"><span>Name</span><span class="line"></span></div>
    <div class="field"><span>Appointment date</span><span class="line"></span></div>
    <div class="field"><span>Time</span><span class="line"></span></div>
    <div class="field"><span>Appointment Location</span><span class="line"></span></div>
  </div>
  <div class="back-brand">
    <span class="brand-dot"></span>
    <span class="brand-name"><span class="main">Brindlecove</span><span class="sub">Nutrition &amp; Dietetics</span></span>
  </div>
</section>

</body>
</html>
```